Berrocal Tizón Law Firm for Small and Medium Business: Website

We need a web design that includes coding for the Wix platform, for a new company based in Santiago, Chile, called Berrocal Tizón, Abogados y Consultores. The company is essentially a law firm, with additional advisory services in accounting, tax management and finance. The main target of the company are founders, CEOs or C-level executives of small or medium companies based in Chile.
The main menu of the web page must have the following tab options:
- Home - About us - Services – How we work -Blog – FAQ -Contact
Our main services are:

1.- Commercial and corporate law advisory
2.- Legal defense in civil, criminal, labor and family matters (litigation and arbitration)
3.- Bankruptcy and reorganization of companies
4.- Collection and recovery of assets
5.- Asset protection
6.- Financial and tax advice

We want to highlight the following services:

-Bankruptcy and reorganization of companies
-Judicial defense in civil matters
-Financial and tax advice

In addition to these services, the following will be offered:
-Lawyer at your home for special cases
-Half hour free consultation
-Monthly service packages

The final design should communicate confidence, business savvy and high execution standards and quality.

Target Market(s)

The main target of the company are founders, CEOs or C-level executives of small or medium companies based in Chile.

Industry/Entity Type

Legal industry

Coding

Number of Pages Required

5+ page

Font styles to use
Serif

Requirements
Must have
• 1. Big banners para destacar los siguientes servicios: -Bankruptcy and reorganization of companies -Judicial defense in civil matters -Financial and tax advice 2. Call to action para agendar consulta legal. 3. Destacar los siguientes servicios: -Lawyer at your home for special cases -Half hour free consultation -Monthly service packages 3. Página para explicar cómo se cobra (precios transparentes): ver el siguiente sitio web: https://www.brookvanelegal.example/how 4. Links to Facebook, Instagram and Linkedin 5. Connection to Whatsapp.
Should not have
• Look old fashioned

```html
<!DOCTYPE html>
<html lang="en">
<head>
<meta charset="utf-8">
<title>Berrocal Tizón — Abogados y Consultores</title>
<link href="https://fonts.googleapis.com/css2?family=Cinzel:wght@400;500;700&family=Montserrat:wght@300;400;500;600;700&display=swap" rel="stylesheet">
<style>
:root{
  --green:#183a2f;
  --green-deep:#12302a;
  --gold:#c8b04c;
  --gold-light:#e6d77a;
  --gold-dark:#a98f32;
  --navy:#142b45;
  --blue:#2a4a7a;
  --blue-soft:#a9c0d9;
  --text:#3d4146;
  --muted:#6b7076;
  --paper:#ffffff;
  --mist:#eef2f3;
}
*{box-sizing:border-box;margin:0;padding:0}
html,body{width:1200px;height:5063px;overflow:hidden}
body{position:relative;background:var(--paper);font-family:"Montserrat",sans-serif;color:var(--text)}
.abs{position:absolute}
section,header,footer{position:absolute;left:0;width:1200px;overflow:hidden}

/* top bar */
.topbar{top:0;height:28px;background:var(--green);color:#fff;font-size:12px}
.topbar .wa{left:102px;top:5px;display:flex;align-items:center;gap:8px}
.topbar .wa b{font-weight:600}
.dot-ic{width:18px;height:18px;border-radius:50%;background:var(--gold);display:inline-flex;align-items:center;justify-content:center}
.topbar .social{left:925px;top:7px;font-size:11px;display:flex;align-items:center;gap:14px}
.topbar .social i{width:10px;height:10px;border-radius:50%;background:#fff;display:inline-block}

/* hero */
.hero{top:0;height:694px;background:var(--mist)}
.hero-photo{left:0;top:0;width:1200px;height:694px;background:linear-gradient(90deg,#f1f3f3 0%,#eceeef 35%,#d7dcdd 55%,#b6b9b2 72%,#c7c1b5 85%,#e4e6e4 100%)}
.nav{top:0;height:118px;left:0;width:1200px}
.logo{left:104px;top:56px;display:flex;align-items:center;gap:10px;font-family:"Cinzel",serif;font-size:24px;color:var(--gold-dark)}
.logo span.sq{width:36px;height:36px;background:var(--gold);display:block}
.menu{top:68px;font-size:12px;font-weight:600;color:#1c1c1c;letter-spacing:.3px}
.menu.active{color:var(--gold)}
.btn-contact{left:976px;top:59px;width:112px;height:34px;background:var(--green);color:#fff;font-size:11px;font-weight:600;display:flex;align-items:center;justify-content:center;border:2px solid #fff;outline:1px solid var(--green)}
.hero .kicker{left:118px;top:244px;font-size:16px;color:var(--green);letter-spacing:.5px}
.hero h1{left:110px;top:270px;font-family:"Cinzel",serif;font-weight:400;font-size:56px;line-height:54px;color:var(--green)}
.hero p{left:118px;top:398px;width:420px;font-size:14px;line-height:25px;color:#333}
.btn-gold{background:linear-gradient(90deg,var(--gold-light),var(--gold));color:#fff;font-size:12px;font-weight:600;display:flex;align-items:center;justify-content:center;letter-spacing:.5px}
.hero .btn-gold{left:120px;top:470px;width:173px;height:40px;font-size:13px}
.chev{width:22px;height:22px}

/* about */
.about{top:694px;height:585px;background:#fff}
.about .gold-block{left:100px;top:74px;width:140px;height:378px;background:var(--gold)}
.about .photo{left:122px;top:92px;width:457px;height:418px;background:linear-gradient(135deg,#5c6f86 0%,#9aa8b5 40%,#dfe3e6 65%,#8392a6 100%);box-shadow:0 14px 30px rgba(0,0,0,.2)}
.kick-gold{font-family:"Cinzel",serif;font-size:14px;letter-spacing:3px;color:var(--gold)}
.about .kick-gold{left:646px;top:156px}
.about h2{left:646px;top:180px;font-family:"Cinzel",serif;font-weight:400;font-size:32px;color:#1b1b1b}
.about h2 b{font-weight:500}
.about .rule{left:646px;top:228px;width:44px;height:2px;background:var(--gold)}
.about p{left:646px;top:256px;width:420px;font-size:14px;line-height:28.5px;color:#444}
.about .btn-gold{left:646px;top:398px;width:165px;height:36px}

/* services */
.services{top:1279px;height:671px;background:linear-gradient(180deg,#e7ecef 0%,#f3f5f6 60%,#e5eaec 100%)}
.services .bg-photo{left:0;top:0;width:1200px;height:671px;background:linear-gradient(90deg,rgba(210,220,226,.7),rgba(240,243,245,.2) 40%,rgba(240,243,245,.2) 60%,rgba(205,215,220,.7))}
.services .kick-gold{left:0;width:1200px;text-align:center;top:48px}
.services h2{left:0;width:1200px;text-align:center;top:66px;font-family:"Cinzel",serif;font-weight:400;font-size:32px;color:#1b1b1b}
.services h2 b{font-weight:500}
.services .rule{left:578px;top:111px;width:44px;height:3px;background:var(--gold)}
.card{background:#fff;box-shadow:0 8px 24px rgba(0,0,0,.1)}
.card .img{position:absolute;left:10px;top:10px;right:10px;height:188px}
.card .badge{position:absolute;width:72px;height:72px;border-radius:50%;border:4px solid #fff;box-shadow:0 3px 8px rgba(0,0,0,.2);display:flex;align-items:center;justify-content:center}
.card h3{position:absolute;left:0;width:100%;text-align:center;font-family:"Cinzel",serif;font-weight:400;color:#1c1c1c}
.card p{position:absolute;left:0;width:100%;text-align:center;font-size:11px;line-height:15px;color:#444;padding:0 40px}

/* how we work */
.how{top:1950px;height:1153px;background:#fff}
.how .kicker{left:0;width:1200px;text-align:center;top:55px;font-size:14px;color:var(--gold);letter-spacing:1px}
.how h2{left:0;width:1200px;text-align:center;top:78px;font-family:"Cinzel",serif;font-weight:400;font-size:30px;color:var(--green);letter-spacing:1px}
.how h2 b{font-weight:700}
.num{font-size:66px;font-weight:300;color:transparent;-webkit-text-stroke:1.5px var(--blue-soft);line-height:1}
.step-title{font-size:20px;font-weight:700;color:var(--blue);line-height:22px;text-align:center}
.step-text{font-size:12px;line-height:19px;color:#444}

/* testimonial */
.testi{top:3103px;height:560px;background:#fff}
.testi h2{left:0;width:1200px;text-align:center;top:98px;font-family:"Cinzel",serif;font-weight:400;font-size:28px;color:#fff}
.testi .rule{left:577px;top:140px;width:46px;height:2px;background:#fff}
.testi .card-q{left:324px;top:191px;width:581px;height:214px;background:#fff;border-radius:14px;text-align:center}
.testi .card-q p{position:absolute;left:40px;right:40px;top:60px;font-size:14px;line-height:25px;color:#444}
.testi .who{position:absolute;left:0;width:100%;top:150px;font-size:14px;font-weight:600;color:#222}
.testi .role{position:absolute;left:0;width:100%;top:172px;font-size:10px;font-weight:700;color:#222}
.avatar{left:587px;top:168px;width:56px;height:56px;border-radius:50%;border:3px solid #fff;background:linear-gradient(135deg,#c8a98a,#8d7a6b)}

/* blog */
.blog{top:3653px;height:540px;background:#fff}
.blog h2{left:0;width:1200px;text-align:center;top:24px;font-family:"Cinzel",serif;font-weight:400;font-size:30px;color:#1b1b1b}
.post{top:84px;width:304px;height:364px;background:#fff;border:1px solid #e3e3e3;box-shadow:0 6px 16px rgba(0,0,0,.06)}
.post .img{position:absolute;left:0;top:0;width:100%;height:182px}
.post .date{position:absolute;left:26px;top:199px;font-size:10px;font-weight:600;color:var(--gold);display:flex;align-items:center;gap:6px}
.post h3{position:absolute;left:26px;top:222px;width:260px;font-size:13px;font-weight:700;line-height:19px;color:#1b1b1b}
.post p{position:absolute;left:26px;top:264px;width:250px;font-size:11px;line-height:17px;color:#555}
.btn-line{position:absolute;left:26px;top:311px;width:108px;height:29px;border:2px solid var(--green);font-size:10px;font-weight:700;color:var(--green);display:flex;align-items:center;justify-content:center}

/* contact */
.contact{top:4193px;height:531px;background:#fff}
.contact .photo{left:420px;top:0;width:780px;height:531px;background:linear-gradient(90deg,#f4f6f8 0%,#c9d3de 25%,#5a7194 55%,#2f4a78 75%,#d9dee3 100%)}
.contact .fade{left:0;top:0;width:760px;height:531px;background:linear-gradient(90deg,#fff 0%,#fff 60%,rgba(255,255,255,0) 100%)}
.contact h2{left:140px;top:96px;font-family:"Cinzel",serif;font-weight:400;font-size:28px;line-height:30px;color:#1b1b1b}
.field{height:37px;border:1px solid #d6d9dc;background:#fff;font-size:11px;color:#6a84a6;display:flex;align-items:center;gap:8px;padding-left:16px}
.contact .btn-gold{left:145px;top:369px;width:170px;height:37px;font-size:11px;gap:6px}

/* footer */
.footer{top:4724px;height:274px;background:var(--green-deep)}
.footer h4{font-size:13px;font-weight:700;color:#fff;letter-spacing:.5px}
.footer li{list-style:none;font-size:11px;color:#fff;line-height:20.5px}
.footer .info{left:110px;font-size:13px;color:#fff;display:flex;align-items:center;gap:10px}
.footer .field{left:738px;top:90px;width:217px;height:33px;font-size:10px;color:#333;padding-left:14px}
.footer .sub{left:738px;top:135px;width:217px;height:30px;font-size:10px}
.footer .circ{width:25px;height:25px;border-radius:50%;background:#fff;top:86px}
.copy{top:4998px;height:65px;background:var(--navy);color:#8fa0b5;font-size:11px;text-align:center;line-height:65px}
</style>
</head>
<body>

<section class="hero">
  <div class="abs hero-photo" role="img" aria-label="Older couple reviewing documents together at a laptop in a bright office"></div>
  <svg class="abs chev" style="left:38px;top:350px" viewBox="0 0 22 22"><path d="M15 3 L6 11 L15 19" fill="none" stroke="#9aa0a4" stroke-width="3"/></svg>
  <svg class="abs chev" style="left:1150px;top:350px" viewBox="0 0 22 22"><path d="M7 3 L16 11 L7 19" fill="none" stroke="#fff" stroke-width="3"/></svg>
  <div class="abs kicker">WELCOME TO BERROCAL TIZÓN</div>
  <h1 class="abs">FINANCE AND<br>TAX ADVICE</h1>
  <p class="abs">Lorem Ipsum is simply dummy text of the printing and typesetting industry. Lorem Ipsum has been the</p>
  <div class="abs btn-gold">LEARN MORE</div>
</section>

<header class="topbar">
  <div class="abs wa"><span class="dot-ic"><svg width="10" height="10" viewBox="0 0 24 24"><path d="M6.6 10.8a15 15 0 0 0 6.6 6.6l2.2-2.2a1 1 0 0 1 1-.25 11.4 11.4 0 0 0 3.6.57 1 1 0 0 1 1 1V20a1 1 0 0 1-1 1A17 17 0 0 1 3 4a1 1 0 0 1 1-1h3.5a1 1 0 0 1 1 1c0 1.25.2 2.45.57 3.57a1 1 0 0 1-.25 1z" fill="#fff"/></svg></span>WHATS APP: <b>(684) 555 0172</b></div>
  <div class="abs social">Visit our social <i></i><i></i><i></i></div>
</header>

<nav class="nav abs">
  <div class="abs logo"><span class="sq"></span>Berrocal Tizón</div>
  <div class="abs menu active" style="left:405px">ABOUT US</div>
  <div class="abs menu" style="left:528px">SERVICES</div>
  <div class="abs menu" style="left:648px">HOW WE WORK</div>
  <div class="abs menu" style="left:809px">BLOG</div>
  <div class="abs menu" style="left:901px">FAQ</div>
  <div class="abs btn-contact">CONTACT</div>
</nav>

<section class="about">
  <div class="abs gold-block"></div>
  <div class="abs photo" role="img" aria-label="Two business partners smiling while reviewing a tablet in an office"></div>
  <svg class="abs" style="left:890px;top:104px" width="200" height="370" viewBox="0 0 200 370">
    <path d="M4 36 V4 H194 V366 H4 V330" fill="none" stroke="#8aa0c0" stroke-width="2"/>
  </svg>
  <div class="abs kick-gold">WHO WE ARE</div>
  <h2 class="abs">ABOUT <b>BERROCAL TIZÓN</b></h2>
  <div class="abs rule"></div>
  <p class="abs">We know, through our personal experiences gained as leaders, that the first 100 days in a critical transition are a crucible of leadership – when managed well, leaders build cohesive teams that succeed.&nbsp; When managed poorly</p>
  <div class="abs btn-gold">LEARN MORE</div>
</section>

<section class="services">
  <div class="abs bg-photo" role="img" aria-label="Soft, faded office scene with colleagues in the background"></div>
  <div class="abs kick-gold">WHAT WE DO</div>
  <h2 class="abs">OUR <b>SERVICES</b></h2>
  <div class="abs rule"></div>

  <div class="abs" style="left:82px;top:430px;width:60px;height:140px;background:var(--gold)"></div>
  <div class="abs" style="left:972px;top:157px;width:142px;height:160px;background:var(--green)"></div>

  <div class="abs card" style="left:92px;top:169px;width:318px;height:392px">
    <div class="img" role="img" aria-label="Team of colleagues gathered around a laptop" style="background:linear-gradient(135deg,#9fb0bd,#d9dde0 50%,#7a8b99)"></div>
    <div class="badge" style="left:123px;top:161px;background:var(--gold)">
      <svg width="34" height="34" viewBox="0 0 34 34" fill="none" stroke="#fff" stroke-width="1.6"><circle cx="17" cy="9" r="5"/><path d="M8 27v-5a9 9 0 0 1 18 0v5"/><rect x="6" y="22" width="22" height="8"/></svg>
    </div>
    <h3 style="top:266px;font-size:15px;line-height:19px"><b style="font-weight:700">LAWYER AT YOUR HOME</b><br>FOR SPECIAL CASES</h3>
    <p style="top:318px">Lorem ipsum dolor sit amet, consectetur adipiscing elit, sed do</p>
  </div>

  <div class="abs card" style="left:438px;top:155px;width:318px;height:432px">
    <div class="img" role="img" aria-label="Colleagues talking at a desk with computers" style="background:linear-gradient(135deg,#5d6a70,#a79d8c 50%,#34414a)"></div>
    <div class="badge" style="left:123px;top:171px;background:var(--green)">
      <svg width="34" height="34" viewBox="0 0 34 34" fill="none" stroke="#fff" stroke-width="1.6"><circle cx="17" cy="17" r="6"/><circle cx="17" cy="17" r="12" stroke-dasharray="3 3"/></svg>
    </div>
    <h3 style="top:278px;font-size:18px;line-height:26px"><b style="font-weight:700">HALF HOUR FREE</b><br>CONSULTATION</h3>
    <p style="top:338px">Lorem ipsum dolor sit amet, consectetur adipiscing elit, sed do</p>
    <div style="position:absolute;left:88px;top:375px;width:150px;height:35px;background:var(--green);color:#fff;font-size:11px;font-weight:600;display:flex;align-items:center;justify-content:center;border:2px solid #fff;outline:1px solid var(--green)">LEARN MORE</div>
  </div>

  <div class="abs card" style="left:784px;top:169px;width:318px;height:392px">
    <div class="img" role="img" aria-label="Business team celebrating with a high five" style="background:linear-gradient(135deg,#b7bec4,#e0e2e2 50%,#6f7780)"></div>
    <div class="badge" style="left:123px;top:161px;background:var(--gold)">
      <svg width="34" height="34" viewBox="0 0 34 34" fill="none" stroke="#fff" stroke-width="1.6"><path d="M10 24 L24 10 M18 10 H24 V16"/><circle cx="12" cy="22" r="3"/></svg>
    </div>
    <h3 style="top:266px;font-size:15px;line-height:19px"><b style="font-weight:700">MONTHLY SERVICE</b><br>PACKAGES</h3>
    <p style="top:318px">Lorem ipsum dolor sit amet, consectetur adipiscing elit, sed do</p>
  </div>
</section>

<section class="how">
  <div class="abs kicker">HOW WE WORK</div>
  <h2 class="abs">HOW WE HELP <b>YOU SUCCEED</b></h2>
  <svg class="abs" style="left:0;top:0" width="1200" height="1153" viewBox="0 0 1200 1153">
    <defs>
      <linearGradient id="goldGrad" x1="0" y1="0" x2="1" y2="1">
        <stop offset="0" stop-color="#efe29a"/><stop offset=".5" stop-color="#c8b04c"/><stop offset="1" stop-color="#9c8430"/>
      </linearGradient>
      <radialGradient id="greenGrad" cx=".4" cy=".35" r=".7">
        <stop offset="0" stop-color="#1f4a3c"/><stop offset="1" stop-color="#0f2d24"/>
      </radialGradient>
    </defs>
    <path d="M648 100 C650 165 620 180 560 180 A140 140 0 0 0 560 460 A156 156 0 0 1 579 771 A136 136 0 0 0 600 1040 Q 690 1055 695 1094" fill="none" stroke="#d6dadd" stroke-width="3"/>
    <circle cx="386" cy="220" r="16" fill="#d8dadc"/>
    <circle cx="864" cy="511" r="6" fill="#8fbfb0"/>
    <circle cx="408" cy="998" r="15" fill="#d3e8df"/>
    <circle cx="695" cy="1094" r="5" fill="#4d7a6f"/>

    <circle cx="560" cy="320" r="104" fill="#eef3f1"/>
    <circle cx="560" cy="320" r="85" fill="url(#goldGrad)"/>
    <g fill="none" stroke="#1c2a3a" stroke-width="2" transform="translate(520 282)">
      <circle cx="15" cy="15" r="9"/><circle cx="15" cy="15" r="3"/><rect x="30" y="10" width="30" height="10" rx="5"/>
      <rect x="8" y="32" width="40" height="10" rx="5"/><rect x="8" y="54" width="26" height="10" rx="5"/><circle cx="58" cy="58" r="12"/><path d="M52 58 l5 5 8-9"/>
    </g>

    <circle cx="579" cy="621" r="104" fill="#eef3f1"/>
    <circle cx="579" cy="621" r="85" fill="url(#greenGrad)"/>
    <g fill="none" stroke="#fff" stroke-width="2" transform="translate(540 585)">
      <rect x="0" y="0" width="46" height="30" rx="3"/><path d="M10 30 v10 l8-10"/><rect x="28" y="22" width="46" height="30" rx="3" fill="#163d32"/><path d="M64 52 v10 l-8-10"/>
      <path d="M8 10h30M8 18h22M36 32h30M36 40h22"/>
    </g>

    <circle cx="581" cy="898" r="104" fill="#eef3f1"/>
    <circle cx="581" cy="898" r="85" fill="url(#goldGrad)"/>
    <g fill="none" stroke="#1c2a3a" stroke-width="2" transform="translate(541 860)">
      <rect x="6" y="0" width="34" height="22" rx="3"/><path d="M12 22v8l8-8"/>
      <circle cx="14" cy="44" r="6"/><circle cx="40" cy="44" r="6"/><circle cx="66" cy="44" r="6"/>
      <path d="M4 70v-8a10 10 0 0 1 20 0v8M30 70v-8a10 10 0 0 1 20 0v8M56 70v-8a10 10 0 0 1 20 0v8M0 72h80"/>
    </g>
  </svg>

  <div class="abs num" style="left:270px;top:262px">01</div>
  <div class="abs step-title" style="left:210px;top:337px;width:190px">PAY AS YOUR GO</div>
  <p class="abs step-text" style="left:680px;top:286px;width:310px">Lorem Ipsum is simply dummy text of the printing and typesetting industry. Lorem Ipsum has been the industry's standard dummy text ever since the 1500s, when an unknown printer took.</p>

  <p class="abs step-text" style="left:150px;top:592px;width:307px;text-align:right">Lorem Ipsum is simply dummy text of the printing and typesetting industry. Lorem Ipsum has been the industry's standard dummy text ever since the 1500s, when an unknown printer took.</p>
  <div class="abs num" style="left:804px;top:565px">02</div>
  <div class="abs step-title" style="left:755px;top:640px;width:195px">CASE REVIW &amp;<br>MEETING</div>

  <div class="abs num" style="left:270px;top:842px">03</div>
  <div class="abs step-title" style="left:205px;top:917px;width:200px">BEST OUTCOME<br>FOR YOU</div>
  <p class="abs step-text" style="left:703px;top:858px;width:310px">Lorem Ipsum is simply dummy text of the printing and typesetting industry. Lorem Ipsum has been the industry's standard dummy text ever since the 1500s, when an unknown printer took.</p>
</section>

<section class="testi">
  <svg class="abs" style="left:0;top:0" width="1200" height="560" viewBox="0 0 1200 560">
    <defs>
      <linearGradient id="bandGrad" x1="0" y1="0" x2="1" y2="0">
        <stop offset="0" stop-color="#e6d77a"/><stop offset=".55" stop-color="#d2bd5c"/><stop offset="1" stop-color="#a98f32"/>
      </linearGradient>
    </defs>
    <polygon points="0,0 420,0 0,70" fill="#dde4ea"/>
    <polygon points="0,70 1200,0 1200,452 0,535" fill="url(#bandGrad)"/>
    <polygon points="826,487 1200,452 1200,560" fill="#183a2f"/>
  </svg>
  <h2 class="abs">WHAT OUR CLIENT SAYS</h2>
  <div class="abs rule"></div>
  <svg class="abs chev" style="left:183px;top:256px" viewBox="0 0 22 22"><path d="M15 3 L6 11 L15 19" fill="none" stroke="#fff" stroke-width="3"/></svg>
  <svg class="abs chev" style="left:1032px;top:256px" viewBox="0 0 22 22"><path d="M7 3 L16 11 L7 19" fill="none" stroke="#fff" stroke-width="3"/></svg>
  <div class="abs card-q">
    <p>Lorem Ipsum is simply dummy text of the printing and typesetting industry. Lorem Ipsum has been the industry's standard dummy text ever since the 1500s, when an unknown printer took a galley</p>
    <div class="who">LUCÍA MARENT,</div>
    <div class="role">COO VELMORA HOLDINGS INC</div>
  </div>
  <div class="abs avatar" role="img" aria-label="Client portrait"></div>
</section>

<section class="blog">
  <h2 class="abs">LATEST BLOG POST</h2>
  <article class="abs post" style="left:136px">
    <div class="img" role="img" aria-label="Colleagues smiling while working on a laptop" style="background:linear-gradient(135deg,#a8b6c2,#e6e8e9 50%,#8798a6)"></div>
    <div class="date"><svg width="11" height="11" viewBox="0 0 12 12" fill="none" stroke="#c8b04c" stroke-width="1.4"><rect x="1" y="2" width="10" height="9"/><path d="M1 5h10M4 0v3M8 0v3"/></svg>15TH JUNE 2021</div>
    <h3>LOREM IPSUM IS SIMPLY DUMMY TEXT OF THE PRINTING</h3>
    <p>Lorem Ipsum is simply dummy text of the printing and typesetting industry.</p>
    <div class="btn-line">LEARN MORE</div>
  </article>
  <article class="abs post" style="left:462px">
    <div class="img" role="img" aria-label="Businesswoman presenting to colleagues at a table" style="background:linear-gradient(135deg,#7d8790,#d8d9d8 50%,#545d66)"></div>
    <div class="date"><svg width="11" height="11" viewBox="0 0 12 12" fill="none" stroke="#c8b04c" stroke-width="1.4"><rect x="1" y="2" width="10" height="9"/><path d="M1 5h10M4 0v3M8 0v3"/></svg>10TH JUNE 2021</div>
    <h3>LOREM IPSUM IS SIMPLY DUMMY TEXT OF THE PRINTING</h3>
    <p>Lorem Ipsum is simply dummy text of the printing and typesetting industry.</p>
    <div class="btn-line">LEARN MORE</div>
  </article>
  <article class="abs post" style="left:786px">
    <div class="img" role="img" aria-label="Team meeting around a laptop in a modern office" style="background:linear-gradient(135deg,#8f9a8f,#dfe2e0 50%,#5e6a70)"></div>
    <div class="date"><svg width="11" height="11" viewBox="0 0 12 12" fill="none" stroke="#c8b04c" stroke-width="1.4"><rect x="1" y="2" width="10" height="9"/><path d="M1 5h10M4 0v3M8 0v3"/></svg>08TH JUNE 2021</div>
    <h3>LOREM IPSUM IS SIMPLY DUMMY TEXT OF THE PRINTING</h3>
    <p>Lorem Ipsum is simply dummy text of the printing and typesetting industry.</p>
    <div class="btn-line">LEARN MORE</div>
  </article>
</section>

<section class="contact">
  <div class="abs photo" role="img" aria-label="Smiling partner in a navy suit holding a phone"></div>
  <div class="abs fade"></div>
  <h2 class="abs">SPEAK TO ONE OF<br>OUR PARTNERS TODAY</h2>
  <div class="abs field" style="left:143px;top:183px;width:228px"><svg width="10" height="10" viewBox="0 0 10 10" fill="#9aa9bb"><circle cx="5" cy="3" r="2.5"/><path d="M0 10a5 5 0 0 1 10 0z"/></svg>First Name</div>
  <div class="abs field" style="left:379px;top:183px;width:228px"><svg width="11" height="9" viewBox="0 0 11 9" fill="none" stroke="#9aa9bb"><rect x=".5" y=".5" width="10" height="8"/><path d="M.5 .5l5 4 5-4"/></svg>E-mail</div>
  <div class="abs field" style="left:143px;top:230px;width:228px"><svg width="10" height="10" viewBox="0 0 10 10" fill="#9aa9bb"><circle cx="5" cy="3" r="2.5"/><path d="M0 10a5 5 0 0 1 10 0z"/></svg>Last Name</div>
  <div class="abs field" style="left:379px;top:230px;width:228px"><svg width="10" height="10" viewBox="0 0 24 24" fill="#9aa9bb"><path d="M6.6 10.8a15 15 0 0 0 6.6 6.6l2.2-2.2a1 1 0 0 1 1-.25 11.4 11.4 0 0 0 3.6.57 1 1 0 0 1 1 1V20a1 1 0 0 1-1 1A17 17 0 0 1 3 4a1 1 0 0 1 1-1h3.5a1 1 0 0 1 1 1c0 1.25.2 2.45.57 3.57a1 1 0 0 1-.25 1z"/></svg>Phone</div>
  <div class="abs field" style="left:143px;top:277px;width:464px;height:73px;align-items:flex-start;padding-top:12px">Leave Message</div>
  <div class="abs btn-gold">SUBMIT MESSAGE <svg width="10" height="10" viewBox="0 0 10 10" fill="#fff"><path d="M0 4 L10 0 L6 10 L5 5z"/></svg></div>
</section>

<footer class="footer">
  <div class="abs info" style="top:117px"><span class="dot-ic" style="width:24px;height:24px"><svg width="11" height="11" viewBox="0 0 24 24"><path d="M6.6 10.8a15 15 0 0 0 6.6 6.6l2.2-2.2a1 1 0 0 1 1-.25 11.4 11.4 0 0 0 3.6.57 1 1 0 0 1 1 1V20a1 1 0 0 1-1 1A17 17 0 0 1 3 4a1 1 0 0 1 1-1h3.5a1 1 0 0 1 1 1c0 1.25.2 2.45.57 3.57a1 1 0 0 1-.25 1z" fill="#fff"/></svg></span>Tel: (1300) 555 0186</div>
  <div class="abs info" style="top:146px"><span class="dot-ic" style="width:24px;height:24px"><svg width="11" height="9" viewBox="0 0 11 9" fill="none" stroke="#fff"><rect x=".5" y=".5" width="10" height="8"/><path d="M.5 .5l5 4 5-4"/></svg></span>Email: info@northvalepartners.example</div>

  <h4 class="abs" style="left:424px;top:56px">NAVIGATE</h4>
  <ul class="abs" style="left:424px;top:82px"><li>Who we are</li><li>What We Do</li><li>Clients</li><li>Blog</li></ul>

  <h4 class="abs" style="left:579px;top:58px">EXPLORE</h4>
  <ul class="abs" style="left:579px;top:84px"><li>Resources</li><li>Why we are</li><li>Terms</li><li>Contact Us</li></ul>

  <h4 class="abs" style="left:733px;top:62px">SIGN UP NEWSLETTER</h4>
  <div class="abs field">EMAIL ADDRESS</div>
  <div class="abs btn-gold sub">SUBSCRIBE</div>

  <h4 class="abs" style="left:1000px;top:56px">FOLLOW US</h4>
  <div class="abs circ" style="left:998px"></div>
  <div class="abs circ" style="left:1025px"></div>
  <div class="abs circ" style="left:1053px"></div>
</footer>
<div class="abs copy" style="left:0;width:1200px">Copyright 2021 Northvale Partners All Right Reserved</div>

</body>
</html>
```